Expense Tracker App for Young Adults

I need a mobile app designer to design an app UI for me. It is for an expense tracker app. I’ve attached a mind map of the various screens and features of the app.

I would like to see designs for this app which is targeted towards young adults (late teens & early 20s) just starting their career who want to plan their budgets and track their expenses.
Updates

Hello designers! I'm conscious that this is not a guaranteed project, so I can understand that some of you might be apprehensive. Just wanted to let you know that I'm willing to see your initial drafts that show your direction and theme for design. You don't have to design the whole app. In fact, it's better if you share your initial design ideas so that we can have a discussion and I can give my input. If I see some good initial designs, I will be happy to make this a guaranteed project. I'm simply being cautious since I'm bootstrapping this and funding out of my own pocket. Thank you for your understanding!

Target Market(s)

Young adults who are just starting their careers, late teens and early 20s.

Font styles to use
Sans Serif

Requirements
Must have
• Ease of use, smart and sleek, a guided setup wizard which will help users setup their account after signing up.
Should not have
• Clunky

```html
<!DOCTYPE html>
<html lang="en">
<head>
<meta charset="utf-8">
<title>Setup – Recurring savings</title>
<link rel="stylesheet" href="https://fonts.googleapis.com/css2?family=Rubik:wght@500;600;700&family=Lato:wght@400&display=swap">
<style>
:root{
  --ink:#22262e;
  --purple:#722f7a;
  --teal:#22bbb0;
  --track:#f2f2f2;
  --border:#d9d9d9;
  --bg:#ffffff;
}
*{margin:0;padding:0;box-sizing:border-box}
html,body{width:1200px;height:2598px;overflow:hidden;background:var(--bg)}
body{position:relative;font-family:'Rubik',sans-serif;color:var(--ink)}
.status-time{position:absolute;left:106px;top:48px;font-family:'Lato',sans-serif;font-size:42px;color:var(--ink)}
.status-icons{position:absolute;left:928px;top:50px}
.header{position:absolute;left:96px;top:218px;display:flex;align-items:center}
.back{width:30px;height:52px}
.title{margin-left:50px;font-size:52px;font-weight:600;line-height:1}
.progress{position:absolute;left:88px;top:466px;display:flex;gap:14px}
.progress span{width:159px;height:15px;border-radius:8px;background:var(--track)}
.progress .done{background:var(--purple)}
.progress .current{background:var(--teal)}
.question{position:absolute;left:96px;top:625px;width:1000px;font-size:50px;font-weight:500;line-height:64px}
.options{position:absolute;left:96px;top:858px;display:flex;gap:72px}
.option{width:466px;height:172px;border:3px solid var(--border);border-radius:70px;background:var(--bg);display:flex;align-items:center;justify-content:center;font-family:'Rubik',sans-serif;font-size:50px;font-weight:700;color:var(--ink)}
.next{position:absolute;left:96px;top:2268px;width:1008px;height:172px;border:none;border-radius:86px;background:var(--purple);color:#fff;font-family:'Rubik',sans-serif;font-size:56px;font-weight:700;letter-spacing:1px}
</style>
</head>
<body>
<div class="status-time">9:41</div>
<svg class="status-icons" width="218" height="40" viewBox="0 0 218 40" aria-hidden="true">
  <g fill="#22262e">
    <rect x="0" y="26" width="10" height="12" rx="2"/>
    <rect x="15" y="19" width="10" height="19" rx="2"/>
    <rect x="30" y="12" width="10" height="26" rx="2"/>
    <rect x="45" y="4" width="10" height="34" rx="2"/>
    <path d="M97 36 l-7-8 a10 10 0 0 1 14 0z"/>
    <path d="M81 22 a23 23 0 0 1 32 0 l-5 5 a16 16 0 0 0-22 0z"/>
    <path d="M72 13 a36 36 0 0 1 50 0 l-5 5 a29 29 0 0 0-40 0z"/>
    <rect x="141" y="6" width="62" height="28" rx="6"/>
    <path d="M211 14 a4 6 0 0 1 0 12z" opacity=".4"/>
  </g>
  <rect x="137" y="2" width="70" height="36" rx="9" fill="none" stroke="#22262e" stroke-opacity=".4" stroke-width="3"/>
</svg>

<header class="header">
  <svg class="back" viewBox="0 0 30 52" aria-label="Back"><path d="M24 4 L6 26 L24 48" fill="none" stroke="#22262e" stroke-width="6" stroke-linecap="round" stroke-linejoin="round"/></svg>
  <h1 class="title">Setup</h1>
</header>

<div class="progress" aria-label="Step 5 of 6">
  <span class="done"></span><span class="done"></span><span class="done"></span><span class="done"></span><span class="current"></span><span></span>
</div>

<h2 class="question">Do you have any recurring savings or investments?</h2>

<div class="options">
  <button class="option">Mutual Fund</button>
  <button class="option">Deposit</button>
</div>

<button class="next">Next</button>
</body>
</html>
```